Business card design needed

Hearthside Comfort Network is a not-for- profit organisation which advocates for palliative care in the community and runs a good size volunteer program to the community. We also run day hospice centres, provide massage & podiatry to clients etc. Our current business cards are very old fashioned and a new look is timely to some positive changes bringing the organisation forward.
Updates

Hi everyone, Thank you all so much for submitting your very clever designs.  I will confer with my colleagues tomorrow and hopefully we can make a decision :)

Industry/Entity Type

Massage

Contact Information for Business Card

Brenna Oakes
Operations Manager
T 02 6184 3920
M 0417526804
E Brenna@hearthsidenet.org.au

Logo Text

Hearthside Comfort Network Inc

Logo styles of interest
Pictorial/Combination Logo
Requirements
Must have
• Our logo (I think I have attached it, contact me if it didn't work)

```html
<!DOCTYPE html>
<html lang="en">
<head>
<meta charset="utf-8">
<title>Brenna Oakes – Business Card</title>
<link rel="stylesheet" href="https://fonts.googleapis.com/css2?family=Baloo+2:wght@800&family=Noto+Sans:wght@400&display=swap">
<style>
  :root {
    --page-bg: #2a2a2a;
    --card-bg: #221e1c;
    --accent-blue: #0a8fd8;
    --title-white: #ffffff;
    --contact-text: #d9d9d9;
    --label-bar: #5e5e5e;
    --label-text: #e6e6e6;
  }
  * { margin: 0; padding: 0; box-sizing: border-box; }
  html, body {
    width: 1200px;
    height: 1050px;
    overflow: hidden;
    background: var(--page-bg);
  }
  .business-card {
    position: absolute;
    left: 150px;
    top: 268px;
    width: 900px;
    height: 514px;
    background: var(--card-bg);
    box-shadow: 0 18px 40px rgba(0,0,0,0.45);
  }
  .card-heading {
    position: absolute;
    left: 46px;
    top: 34px;
    font-family: "Baloo 2", sans-serif;
    font-weight: 800;
    line-height: 1;
  }
  .holder-name {
    color: var(--accent-blue);
    font-size: 36px;
    margin-left: 14px;
  }
  .holder-role {
    color: var(--title-white);
    font-size: 40px;
    margin-top: 4px;
  }
  .contact-block {
    position: absolute;
    left: 54px;
    top: 290px;
    display: flex;
    align-items: stretch;
    font-family: "Noto Sans", sans-serif;
  }
  .contact-labels {
    width: 22px;
    background: var(--label-bar);
    color: var(--label-text);
    font-size: 14px;
    display: flex;
    flex-direction: column;
    align-items: center;
    justify-content: space-around;
    padding: 4px 0;
  }
  .contact-values {
    padding-left: 10px;
    color: var(--contact-text);
    font-size: 17px;
    line-height: 25px;
    padding-top: 8px;
  }
</style>
</head>
<body>
  <section class="business-card">
    <header class="card-heading">
      <h1 class="holder-name">Brenna Oakes</h1>
      <p class="holder-role">Operations Manager</p>
    </header>
    <div class="contact-block">
      <div class="contact-labels">
        <span>T</span><span>M</span><span>E</span>
      </div>
      <div class="contact-values">
        <p>02 6184 3920</p>
        <p>04 1752 6804</p>
        <p>Brenna@hearthsidenet.org.au</p>
      </div>
    </div>
  </section>
</body>
</html>
```